Business Card Design Project

Company Name - Larkmere Med

Wellness consulting and training company. Run through a medical centre.

Main colour themes are orange and blue, as in the logo. Want to replicate same effect with business cards.

To give a sense of freedom and potential as per the company name.

Want the business card to be in line with stationary design, which I have launched as well.

Double sided with design and colour on one side and details on other side.
Updates

Reason: Need business card and stationary design to be teed up.

Target Market(s)

35 to 65 age group.
New age and trendy

Industry/Entity Type

Training

Requirements
Must have
• Colours orange and blue as per logo
Nice to have
• Design to be similar to stationary design, letterhead and envelopes

```html
<!DOCTYPE html>
<html lang="en">
<head>
<meta charset="utf-8">
<title>Larkmere Med – Business Card</title>
<link rel="stylesheet" href="https://fonts.googleapis.com/css2?family=Abel&display=swap">
<style>
  :root {
    --page-bg: #d9d9d9;
    --navy-deep: #0f2a5e;
    --navy: #173a80;
    --navy-light: #2a57a8;
    --brand-blue: #1f4f9e;
    --muted-blue: #5c7fb8;
    --orange: #f26a1b;
    --paper: #fafafa;
    --paper-shade: #ececec;
    --ink-light: #e8eef8;
    --divider: rgba(255,255,255,0.35);
  }
  * { box-sizing: border-box; margin: 0; padding: 0; }
  html, body {
    width: 1200px; height: 900px; overflow: hidden;
    background: var(--page-bg);
    font-family: "Abel", "Arial Narrow", sans-serif;
  }
  .canvas { position: relative; width: 1200px; height: 900px; }

  .card {
    position: absolute;
    width: 540px; height: 310px;
    overflow: hidden;
    box-shadow: 0 6px 18px rgba(0,0,0,0.25);
  }

  /* Front side */
  .card--front {
    left: 90px; top: 110px;
    background:
      radial-gradient(ellipse 70% 90% at 78% 20%, var(--navy-light) 0%, rgba(42,87,168,0) 70%),
      linear-gradient(135deg, var(--navy-deep) 0%, var(--navy) 100%);
  }
  .card--front .wordmark {
    position: absolute;
    left: 130px; top: 118px;
    font-size: 62px;
    color: var(--ink-light);
    letter-spacing: -1px;
    white-space: nowrap;
  }

  /* Back side */
  .card--back {
    left: 570px; top: 480px;
    background: var(--navy);
  }
  .card__header {
    position: absolute; left: 0; top: 0;
    width: 100%; height: 162px;
    background: linear-gradient(180deg, #ffffff 0%, var(--paper) 60%, var(--paper-shade) 100%);
    border-bottom: 4px solid var(--orange);
  }
  .person { position: absolute; left: 36px; top: 82px; }
  .person__name { font-size: 28px; color: var(--brand-blue); line-height: 1; }
  .person__role { font-size: 20px; color: var(--muted-blue); margin-top: 4px; }

  .card__header .wordmark {
    position: absolute; right: 34px; top: 92px;
    font-size: 30px; color: var(--brand-blue);
    letter-spacing: -0.5px;
    display: flex; align-items: center; gap: 8px;
  }
  .wordmark__dot {
    width: 10px; height: 10px; border-radius: 50%;
    background: var(--orange);
  }

  .card__details {
    position: absolute; left: 0; top: 166px;
    width: 100%; height: 144px;
    background:
      radial-gradient(ellipse 80% 100% at 60% 0%, var(--navy-light) 0%, rgba(42,87,168,0) 75%),
      linear-gradient(180deg, var(--navy) 0%, var(--navy-deep) 100%);
    color: var(--ink-light);
    font-size: 16px;
  }
  .address {
    position: absolute; right: 330px; top: 46px;
    display: flex; gap: 12px; align-items: flex-start;
    text-align: right; line-height: 1.4;
  }
  .address svg { margin-top: 3px; }
  .divider {
    position: absolute; left: 222px; top: 18px;
    width: 1px; height: 106px;
    background: var(--divider);
  }
  .contact {
    position: absolute; left: 244px; top: 26px;
    list-style: none;
  }
  .contact li {
    display: flex; align-items: center; gap: 12px;
    height: 28px;
  }
  .icon { width: 14px; height: 14px; fill: var(--ink-light); flex: none; }
</style>
</head>
<body>
<main class="canvas">

  <section class="card card--front" aria-label="Business card front">
    <div class="wordmark">Larkmere Med</div>
  </section>

  <section class="card card--back" aria-label="Business card back">
    <header class="card__header">
      <div class="person">
        <div class="person__name">Evan Hartley</div>
        <div class="person__role">President</div>
      </div>
      <div class="wordmark"><span>Larkmere Med</span><span class="wordmark__dot"></span></div>
    </header>

    <div class="card__details">
      <div class="address">
        <svg class="icon" viewBox="0 0 14 14" aria-hidden="true">
          <path d="M7 0a4.5 4.5 0 0 0-4.5 4.5C2.5 8 7 12 7 12s4.5-4 4.5-7.5A4.5 4.5 0 0 0 7 0zm0 6.3a1.8 1.8 0 1 1 0-3.6 1.8 1.8 0 0 1 0 3.6z"/>
          <rect x="1" y="12.6" width="12" height="1.2" rx="0.6"/>
        </svg>
        <div>18 Wexford Lane<br>Sydney, NSW 2000</div>
      </div>

      <div class="divider"></div>

      <ul class="contact">
        <li>
          <svg class="icon" viewBox="0 0 14 14" aria-hidden="true">
            <path d="M4 0h6a1 1 0 0 1 1 1v12a1 1 0 0 1-1 1H4a1 1 0 0 1-1-1V1a1 1 0 0 1 1-1zm.5 1.5v9.5h5V1.5zM7 11.6a.7.7 0 1 0 0 1.4.7.7 0 0 0 0-1.4z"/>
          </svg>
          <span>555-0142-7730</span>
        </li>
        <li>
          <svg class="icon" viewBox="0 0 14 14" aria-hidden="true">
            <path d="M3.5 1h7v3h-7zM1 5h12a1 1 0 0 1 1 1v5h-2.5V9h-9v2H0V6a1 1 0 0 1 1-1zm2.5 5h7v3.5h-7z"/>
          </svg>
          <span>555-0142-7731</span>
        </li>
        <li>
          <svg class="icon" viewBox="0 0 14 14" aria-hidden="true">
            <path d="M0 3h14v8H0zm1.2 1.2L7 8l5.8-3.8V3.9L7 7.4 1.2 3.9z"/>
          </svg>
          <span>info@larkmeremed.com</span>
        </li>
      </ul>
    </div>
  </section>

</main>
</body>
</html>
```